Webdesign für Immobilienmanagement
Zielgruppe
Immobilienmanagement Unternehmen / allg. Hausverwaltung , Hausmeisterservice, Grünanlagenpflege, Unterhaltsreinigung, Winterdienst
Zielgruppe: Mieter und Wohnungseigentümer
Aufgabenstellung
Farben: weiß/grün
keine Kopie der alten Seite
nutzerfreundliche Unternehmenswebseite
Logo vorhanden auf alter Webseite

```html
<!DOCTYPE html>
<html lang="de">
<head>
<meta charset="utf-8">
<title>Grünhof Immobilien-Management</title>
<link href="https://fonts.googleapis.com/css2?family=Ubuntu:wght@500;700&family=Nunito+Sans:wght@400;600;700&display=swap" rel="stylesheet">
<style>
:root{
  --green:#55ad38;
  --green-dark:#4a9a30;
  --navy:#0d3a78;
  --text:#222;
  --muted:#666;
  --light:#999;
  --band:#eef2f7;
  --white:#fff;
  --orange:#f26b3a;
}
*{box-sizing:border-box;margin:0;padding:0}
html,body{width:1200px;height:2573px;overflow:hidden;background:var(--white);font-family:"Nunito Sans",sans-serif;color:var(--text)}
.page{position:relative;width:1200px;height:2573px;overflow:hidden}
.abs{position:absolute}
.heading{font-family:"Ubuntu",sans-serif;font-weight:700;color:var(--green)}

/* nav */
.brand{left:32px;top:5px;width:172px;height:62px;background:#f2f2f2;display:flex;align-items:center;justify-content:center;gap:8px}
.brand-name{font-family:"Ubuntu",sans-serif;font-weight:700;font-size:20px;color:var(--green);letter-spacing:1px}
.brand-mark{width:14px;height:14px;background:var(--green)}
.nav{left:0;top:31px;font-size:13px;color:var(--text)}
.nav a{position:absolute;white-space:nowrap;text-decoration:none;color:var(--text)}
.nav a.active{color:var(--green)}
.saved{left:856px;top:25px;width:118px;height:28px;border:1px dashed #888;border-radius:10px;font-size:13px;display:flex;align-items:center;justify-content:center;gap:5px;color:#333}
.bell{left:989px;top:20px;width:38px;height:38px;border-radius:50%;background:#e8ebf0;display:flex;align-items:center;justify-content:center}
.login{left:1051px;top:21px;width:112px;height:36px;border:2px solid #3a8fd8;border-radius:6px;background:var(--green);color:#fff;font-weight:700;font-size:13px;display:flex;align-items:center;justify-content:center}

/* hero */
.hero-photo{left:294px;top:76px;width:879px;height:582px;border-radius:40px;background:linear-gradient(135deg,#0d3a78 0%,#0e3c7c 35%,#dfe3e8 55%,#c9ced6 75%,#0d3a78 100%)}
.hero-card{left:0;top:145px;width:484px;height:249px;background:#fff;border-radius:0 44px 44px 0}
.hero-title{font-size:56px;line-height:1;position:absolute}
.hero-sub{left:56px;top:333px;font-size:13px;font-weight:700;line-height:17px;width:310px}
.tabs{top:442px}
.tab-buy{left:39px;top:442px;width:85px;height:38px;border-radius:19px;background:var(--green);color:#fff;font-family:"Ubuntu",sans-serif;font-weight:700;font-size:18px;display:flex;align-items:center;justify-content:center}
.tab{top:450px;font-family:"Ubuntu",sans-serif;font-weight:700;font-size:18px;color:#333}
.search-bar{left:28px;top:495px;width:960px;height:87px;background:#fff;border-radius:6px;box-shadow:0 4px 14px rgba(0,0,0,.12)}
.field-label{top:515px;font-size:13px;color:var(--light)}
.field-value{top:543px;font-family:"Ubuntu",sans-serif;font-weight:700;font-size:19px;color:var(--green)}
.advance{left:719px;top:532px;font-size:14px;color:#444}
.search-btn{left:838px;top:517px;width:132px;height:44px;background:var(--green);border-radius:6px;color:#fff;font-size:14px;display:flex;align-items:center;justify-content:center}

/* welcome */
.welcome-title{left:0;width:1226px;text-align:center;top:747px;font-size:32px}
.welcome-text{left:72px;top:786px;width:1100px;font-size:15px;color:var(--muted);line-height:20px}
.welcome-text p{margin-bottom:20px}
.type-card{top:920px;width:240px;height:207px;background:#fff;border-radius:14px;box-shadow:0 2px 12px rgba(0,0,0,.08)}
.type-photo{position:absolute;left:18px;top:22px;width:198px;height:139px;border-radius:14px}
.type-label{position:absolute;left:0;width:230px;top:176px;text-align:center;font-size:15px;color:var(--light)}
.check{position:absolute;left:199px;top:172px;width:27px;height:27px;border-radius:50%;background:var(--orange);display:flex;align-items:center;justify-content:center}
.continue{left:416px;top:1181px;width:369px;height:59px;background:var(--green);border-radius:10px;color:#fff;font-size:18px;display:flex;align-items:center;justify-content:center}

/* services */
.band{left:0;top:1233px;width:1200px;height:697px;background:var(--band)}
.service-box{left:74px;top:1271px;width:1046px;height:436px;background:#fff;border-radius:8px;box-shadow:0 2px 10px rgba(0,0,0,.06)}
.hours{left:146px;top:1332px;width:378px;height:297px;background:var(--green);color:#fff;padding:40px 36px}
.hours h3{font-family:"Ubuntu",sans-serif;font-weight:700;font-size:22px;margin-bottom:18px}
.hours p{font-size:11px;line-height:19.5px;margin-bottom:19px;width:160px}
.services-title{left:720px;top:1355px;font-size:23px;line-height:30px}
.service-list{left:771px;top:1445px;list-style:none;font-family:"Ubuntu",sans-serif;font-weight:500;font-size:14px;color:#777;line-height:22.5px}

/* living */
.frame{left:452px;top:1733px;width:701px;height:532px;background:#fff;border-radius:40px;box-shadow:0 2px 16px rgba(0,0,0,.08)}
.main-photo{left:466px;top:1747px;width:673px;height:504px;border-radius:30px;background:linear-gradient(160deg,#5b5a6e 0%,#8a8ea0 30%,#3f78b8 55%,#9a6a52 80%,#6a4a3a 100%)}
.video-photo{left:372px;top:2010px;width:334px;height:222px;border-radius:30px;background:linear-gradient(135deg,#f4efe8 0%,#d9d2c8 40%,#b8a99a 70%,#8a7868 100%)}
.play{left:502px;top:2085px;width:74px;height:74px;border-radius:50%;background:#fff;display:flex;align-items:center;justify-content:center}
.living-title{left:75px;top:1890px;font-size:40px;line-height:72px}
.see-all{left:74px;top:2054px;width:214px;height:66px;background:var(--green);border-radius:10px;color:#fff;font-size:18px;display:flex;align-items:center;justify-content:center}

/* footer */
.footer{left:3px;top:2323px;width:1197px;height:250px;background:var(--green);color:#fff}
.footer-brand{left:173px;top:41px;width:200px;height:69px;background:#f2f2f2;display:flex;align-items:center;justify-content:center;gap:8px}
.social{top:154px;width:27px;height:27px;border-radius:50%;background:#fff;display:flex;align-items:center;justify-content:center}
.social span{width:9px;height:9px;border-radius:50%;background:#6aa2d8}
.col-title{top:42px;font-size:11px;font-weight:700}
.col-links{top:76px;list-style:none;font-size:9px;line-height:26px}
.contact{left:814px;top:42px;font-size:11px;font-weight:700;line-height:15px}
.legal{top:2547px;font-size:9px;color:#fff}
</style>
</head>
<body>
<div class="page">

  <!-- navigation -->
  <div class="abs brand"><span class="brand-name">GRÜNHOF</span><span class="brand-mark"></span></div>
  <nav class="abs nav">
    <a class="active" style="left:288px">Home</a>
    <a style="left:363px">über uns</a>
    <a style="left:439px">Hausverwaltung</a>
    <a style="left:570px">Hausmeister</a>
    <a style="left:680px">Downloads</a>
    <a style="left:769px">Partnerlinks</a>
  </nav>
  <div class="abs saved">
    <svg width="12" height="12" viewBox="0 0 12 12"><circle cx="5" cy="5" r="3.8" fill="none" stroke="#333" stroke-width="1.3"/><line x1="8" y1="8" x2="11" y2="11" stroke="#333" stroke-width="1.3"/></svg>
    Saved Search
  </div>
  <div class="abs bell">
    <svg width="18" height="18" viewBox="0 0 18 18"><path d="M4 13h10l-1.5-2V7.5a3.5 3.5 0 0 0-7 0V11z" fill="none" stroke="#55ad38" stroke-width="1.5"/><path d="M7.5 15h3" stroke="#55ad38" stroke-width="1.5"/><circle cx="13" cy="4" r="3" fill="#55ad38"/></svg>
  </div>
  <div class="abs login">LOGIN</div>

  <!-- hero -->
  <div class="abs hero-photo" role="img" aria-label="Modernes weißes Wohnhochhaus mit Balkonen vor tiefblauem Himmel"></div>
  <div class="abs hero-card">
    <span class="heading hero-title" style="left:48px;top:30px">Let’s find</span>
    <span class="heading hero-title" style="left:62px;top:104px">yours Dream..</span>
  </div>
  <p class="abs hero-sub">Building award winning properties across London UK and the All world</p>

  <div class="abs tab-buy">Buy</div>
  <span class="abs tab" style="left:147px">Sell</span>
  <span class="abs tab" style="left:214px">Rent</span>

  <div class="abs search-bar"></div>
  <span class="abs field-label" style="left:57px">City/Street</span>
  <span class="abs field-value" style="left:57px">Enter City</span>
  <span class="abs field-label" style="left:224px">Apartment Type</span>
  <span class="abs field-value" style="left:225px">Deluxe Portion
    <svg width="8" height="12" viewBox="0 0 8 12" style="margin-left:8px"><path d="M4 1L7 4.5H1zM4 11L1 7.5h6z" fill="#55ad38"/></svg></span>
  <span class="abs field-label" style="left:418px">Price Range</span>
  <span class="abs field-value" style="left:419px">Min price - Max price
    <svg width="8" height="12" viewBox="0 0 8 12"><path d="M4 1L7 4.5H1zM4 11L1 7.5h6z" fill="#0d3a78"/></svg></span>
  <span class="abs advance">+ Advance Filter</span>
  <div class="abs search-btn">Search</div>

  <!-- welcome -->
  <h2 class="abs heading welcome-title">Herzlich Willkommen</h2>
  <div class="abs welcome-text">
    <p>auf der Homepage der Grünhof Immobilien-Management GmbH!</p>
    <p>Wir sind ein junges, freundliches, gut ausgebildetes Team, das sich mit all seiner Aufmerksamkeit und Kompetenz um Ihre Wünsche in Sachen Immobilien kümmert. Möchten Sie eine Wohnung mieten, suchen Sie einen Hausmeister ... oder einen Verwalter für Ihre Immobilie?</p>
    <p>Schauen Sie sich unser Leistungsangebot an und überzeugen Sie sich selbst von den Vorteilen, die wir Ihnen bieten können.</p>
  </div>

  <div class="abs type-card" style="left:62px">
    <div class="type-photo" role="img" aria-label="Dachterrasse mit Lounge-Möbeln und Bepflanzung" style="background:linear-gradient(135deg,#5f7a3e,#9a9a92 55%,#c4c2bc)"></div>
    <span class="type-label">Deluxe Portion</span>
    <span class="check"><svg width="13" height="10" viewBox="0 0 13 10"><path d="M1.5 5l3.5 3.5 6.5-7" fill="none" stroke="#fff" stroke-width="2"/></svg></span>
  </div>
  <div class="abs type-card" style="left:342px">
    <div class="type-photo" role="img" aria-label="Hohes Wohnzimmer mit Kronleuchter und großen Fenstern" style="background:linear-gradient(135deg,#b7b2a8,#e4e0d8 50%,#6f6c68)"></div>
    <span class="type-label">Double Height</span>
  </div>
  <div class="abs type-card" style="left:622px">
    <div class="type-photo" role="img" aria-label="Penthouse-Terrasse mit Essbereich und Grünpflanzen" style="background:linear-gradient(135deg,#5f7a3e,#9a9a92 55%,#c4c2bc)"></div>
    <span class="type-label">Penthouse</span>
  </div>
  <div class="abs type-card" style="left:902px">
    <div class="type-photo" role="img" aria-label="Helles Studio-Apartment mit Holzboden" style="background:linear-gradient(135deg,#f1efec,#e6e2dc 55%,#c98a4a)"></div>
    <span class="type-label">The Studio</span>
  </div>

  <div class="abs continue">Continue</div>

  <!-- services -->
  <div class="abs band"></div>
  <div class="abs service-box"></div>
  <div class="abs hours">
    <h3>Unsere Geschäftszeiten:</h3>
    <p>Montag<br>09.00 - 12.00 Uhr</p>
    <p>Dienstag<br>09.00 - 12.00 Uhr und 13.00 - 15.00 Uhr</p>
    <p>Donnerstag<br>09.00 - 12.00 Uhr und 13.00 - 18.00 Uhr</p>
  </div>
  <h3 class="abs heading services-title">Ihr zuverlässiger Dienstleister<br>rund um die Immobilie</h3>
  <ul class="abs service-list">
    <li>Allgemeine Hausverwaltung</li>
    <li>Kaufmännische Betreuung</li>
    <li>Technische Betreuung</li>
    <li>Hausmeisterservice</li>
    <li>Grünanlagenpflege</li>
    <li>Unterhaltsreinigung</li>
    <li>Winterdienst</li>
  </ul>

  <!-- living -->
  <div class="abs frame"></div>
  <div class="abs main-photo" role="img" aria-label="Loungebereich mit Sesseln und Panoramafenstern über der Stadt"></div>
  <div class="abs video-photo" role="img" aria-label="Helles Wohnzimmer mit Sofa und Essbereich, Videovorschau"></div>
  <div class="abs play"><svg width="18" height="20" viewBox="0 0 18 20"><path d="M3 2l13 8-13 8z" fill="#55ad38"/></svg></div>
  <h2 class="abs heading living-title">Wohnen und<br><span style="padding-left:10px">arbeiten ...</span></h2>
  <div class="abs see-all">See All</div>

  <!-- footer -->
  <footer class="abs footer">
    <div class="abs footer-brand"><span class="brand-name" style="font-size:24px">GRÜNHOF</span><span class="brand-mark" style="width:16px;height:16px"></span></div>
    <span class="abs social" style="left:204px"><span></span></span>
    <span class="abs social" style="left:238px"><span></span></span>
    <span class="abs social" style="left:272px"><span></span></span>
    <span class="abs social" style="left:306px"><span></span></span>

    <span class="abs col-title" style="left:502px">Useful Links</span>
    <ul class="abs col-links" style="left:502px"><li>About</li><li>Partners</li><li>Contact</li></ul>
    <span class="abs col-title" style="left:647px">Help?</span>
    <ul class="abs col-links" style="left:647px"><li>FAQ</li><li>Term &amp; Condition</li><li>Policy</li><li>Privacy</li></ul>
    <div class="abs contact">Kontakt<br>Impressum<br>Datenschutz</div>
  </footer>
  <span class="abs legal" style="left:256px">© Copyright 2024</span>
  <span class="abs legal" style="left:804px">Terms &amp; Condition &nbsp;&nbsp;|&nbsp;&nbsp; Privacy Policy</span>

</div>
</body>
</html>
```